Valtera Drones webdesign: Innovative Drones service company in agriculture

We need a new website according the following conditions:
• Main colour orange and current logo;
• Transparent – open – trustworthy – dynamic - personal;
• Use the smartness and overview characteristics of the crow (Valtera is Latin for crow);
• Accessible to multiple target groups and markets:
o So not too horticultural, too green;
• Use contradictions:
o Future versus nostalgia;
o Smartness crow versus precision hummingbird;
o Technology versus mechanical;
• Kestam 2.4 GTR as a style icon?
• Long pager website
Updates

Website menu o Home o Crop monitoring  Applications Growth | Stress | Development | Diseases  Markets Breeding | Young plant | Potplants | Cutflowers | Vegetables | Soft fruit  Customer cases o Technology Aerial data collection | Artificial intelligence | Free data sets o About Vision | Company | Partners | Team | Career o Contact o News&downloads Logo: www.valteradrones-example.com

Target Market(s)

agriculture: owners, crop managers
oil&gas: maintenance, quality control managers and purchase managers
logistics: ware house managers, purchase managers

Industry/Entity Type

Agribusiness

Number of Pages Required

2 page

Colors
f78f20

Requirements
Must have
• long pager website
downloads
Netlink
Should not have
• Not too 'green' because first impression of designers of agriculture/horticulture is using the green colour. But that is not necessary.

Keep in mind that the current logo will be updates: the circle will be more 'general' and less 'agri'. Also the green colors in the logo will be slightly darker to make it more powerful.

```html
<!DOCTYPE html>
<html lang="en">
<head>
<meta charset="utf-8">
<title>Valtera Drones – About</title>
<link href="https://fonts.googleapis.com/css2?family=Lato:wght@300;400;700;900&display=swap" rel="stylesheet">
<style>
  :root {
    --orange: #f78f20;
    --text: #666666;
    --text-dark: #555555;
    --rule: #8a8a8a;
    --photo: #dcdcdc;
    --card: #636262;
    --footer: #676666;
    --white: #ffffff;
  }
  * { margin: 0; padding: 0; box-sizing: border-box; }
  html, body { width: 1200px; height: 3438px; overflow: hidden; background: var(--white); }
  body { position: relative; font-family: 'Lato', sans-serif; color: var(--text); }

  .site-header { position: absolute; left: 62px; top: 30px; width: 1053px; height: 48px; }
  .brand { position: absolute; left: 0; top: 0; display: flex; align-items: center; gap: 10px; }
  .brand-mark { width: 44px; height: 44px; border-radius: 50%; background: var(--orange); }
  .brand-name { font-weight: 400; font-size: 24px; color: var(--orange); letter-spacing: 0.5px; }
  .main-nav { position: absolute; right: 0; top: 16px; display: flex; gap: 27px; }
  .main-nav a { font-size: 12px; color: var(--text-dark); text-decoration: none; text-transform: uppercase; }

  .hero { position: absolute; left: 62px; top: 128px; width: 1053px; height: 255px;
    background: linear-gradient(90deg, #5f9a3c 0%, #6fae45 45%, #7fb650 100%); }
  .hero-title { position: absolute; left: 66px; top: 56px; font-weight: 300; font-size: 36px; line-height: 45px; color: var(--white); }

  .section-title { position: absolute; left: 130px; font-weight: 300; font-size: 37px; color: var(--orange); }
  .section-copy { position: absolute; left: 131px; width: 900px; font-weight: 300; font-size: 17px; line-height: 22px; color: var(--text); }
  .section-copy p + p { margin-top: 22px; }
  .divider { position: absolute; left: 62px; width: 1051px; height: 1px; background: var(--rule); }

  .partner { position: absolute; width: 300px; text-align: center; font-weight: 700; font-size: 24px; color: var(--text-dark); transform: translate(-50%, -50%); }

  .member { position: absolute; width: 263px; text-align: center; }
  .member-photo { width: 263px; height: 267px; background: linear-gradient(135deg, #e2e2e2, #cfcfcf); }
  .member-name { margin-top: 16px; font-weight: 400; font-size: 24px; color: var(--text-dark); }
  .member-role { margin-top: 2px; font-size: 14px; color: var(--text-dark); }

  .vacancy { position: absolute; width: 265px; height: 99px; background: var(--card); border-left: 9px solid var(--orange);
    display: flex; align-items: center; padding-left: 15px; font-weight: 700; font-size: 14px; color: var(--white); }

  .site-footer { position: absolute; left: 62px; top: 3155px; width: 1053px; height: 283px; background: var(--footer); color: var(--white); }
  .footer-col { position: absolute; }
  .footer-heading { font-weight: 700; font-size: 17px; letter-spacing: 1px; text-transform: uppercase; }
  .footer-list { list-style: none; font-size: 14px; line-height: 18px; letter-spacing: 0.5px; }
  .footer-contact { font-size: 14px; line-height: 18px; letter-spacing: 0.5px; margin-top: 22px; }
  .social { position: absolute; left: 84px; top: 160px; display: flex; align-items: center; gap: 10px; font-size: 14px; }
  .social-dot { width: 40px; height: 40px; border-radius: 50%; background: var(--white); }
</style>
</head>
<body>

<header class="site-header">
  <div class="brand"><span class="brand-mark"></span><span class="brand-name">Valtera Drones</span></div>
  <nav class="main-nav">
    <a href="#">Home</a><a href="#">Crop monitoring</a><a href="#">Markets</a><a href="#">Customer cases</a>
    <a href="#">Technology</a><a href="#">About</a><a href="#">Contacts</a><a href="#">New &amp; downloads</a>
  </nav>
</header>

<section class="hero" role="img" aria-label="Photo of an orange quadcopter drone hovering above a green field">
  <h1 class="hero-title">Lorem ipsum dolor<br>sit amet, consect<br>etur adipiscing elit.</h1>
</section>

<h2 class="section-title" style="top:398px">Vision</h2>
<div class="section-copy" style="top:456px">
  <p>Lorem ipsum dolor sit amet, consectetur adipiscing elit. Morbi ultricies molestie orci. Aenean purus mauris, sodales nec diam dignissim, porttitor laoreet enim. Aliquam id sollicitudin turpis. Vivamus aliquet elit sem, et ornare ex aliquam in. In cursus, felis non pretium molestie, tellus lacus facilisis metus, ut accumsan nisi nulla accumsan risus. Etiam id pharetra ante. Nunc sit amet ante id justo consequat tempor. Nullam pretium arcu eu hendrerit aliquam. Sed in purus eros.</p>
  <p>Fusce placerat risus sit amet lectus egestas, pretium porttitor nisi facilisis. Morbi pellentesque odio et nulla interdum viverra. Nam suscipit, eros ut vulputate ultrices, libero odio mollis justo, nec varius felis odio ut mi. Sed felis nisl, congue at finibus in, porttitor ut elit. Etiam et mattis ipsum. Praesent vel molestie mi. Duis in nunc nunc. Class aptent taciti sociosqu ad litora torquent per conubia nostra, per inceptos himenaeos. Cras eget leo urna.</p>
</div>
<div class="divider" style="top:725px"></div>

<h2 class="section-title" style="top:745px">Company</h2>
<div class="section-copy" style="top:803px">
  <p>Lorem ipsum dolor sit amet, consectetur adipiscing elit. Morbi ultricies molestie orci. Aenean purus mauris, sodales nec diam dignissim, porttitor laoreet enim. Aliquam id sollicitudin turpis. Vivamus aliquet elit sem, et ornare ex aliquam in. In cursus, felis non pretium molestie, tellus lacus facilisis metus, ut accumsan nisi nulla accumsan risus. Etiam id pharetra ante. Nunc sit amet ante id justo consequat tempor. Nullam pretium arcu eu hendrerit aliquam. Sed in purus eros.</p>
  <p>Fusce placerat risus sit amet lectus egestas, pretium porttitor nisi facilisis. Morbi pellentesque odio et nulla interdum viverra. Nam suscipit, eros ut vulputate ultrices, libero odio mollis justo, nec varius felis odio ut mi. Sed felis nisl, congue at finibus in, porttitor ut elit. Etiam et mattis ipsum. Praesent vel molestie mi. Duis in nunc nunc. Class aptent taciti sociosqu ad litora torquent per conubia nostra, per inceptos himenaeos. Cras eget leo urna.</p>
</div>
<div class="divider" style="top:1072px"></div>

<h2 class="section-title" style="top:1102px">Partners</h2>
<div class="partner" style="left:240px;top:1228px">Brightwing</div>
<div class="partner" style="left:572px;top:1228px">Korvel</div>
<div class="partner" style="left:900px;top:1228px">Meadow Arts Guild</div>
<div class="partner" style="left:240px;top:1408px">Selvane</div>
<div class="partner" style="left:572px;top:1408px">Teatro Nuvola</div>
<div class="partner" style="left:900px;top:1408px">Rivermart</div>
<div class="partner" style="left:240px;top:1608px">Hollow Creek Folk Fair</div>
<div class="partner" style="left:572px;top:1608px">Skyreach Conservancy</div>
<div class="partner" style="left:900px;top:1608px">Savoro</div>
<div class="divider" style="top:1787px"></div>

<h2 class="section-title" style="top:1817px">Team</h2>
<div class="member" style="left:133px;top:1895px"><div class="member-photo" role="img" aria-label="Portrait placeholder"></div><div class="member-name">Tom Harlow</div><div class="member-role">Managing Director</div></div>
<div class="member" style="left:448px;top:1895px"><div class="member-photo" role="img" aria-label="Portrait placeholder"></div><div class="member-name">Ella Marie Voss</div><div class="member-role">Managing Director</div></div>
<div class="member" style="left:771px;top:1895px"><div class="member-photo" role="img" aria-label="Portrait placeholder"></div><div class="member-name">Peter Lindqvist</div><div class="member-role">Chief Technology Officer</div></div>
<div class="member" style="left:133px;top:2258px"><div class="member-photo" role="img" aria-label="Portrait placeholder"></div><div class="member-name">Daan Brenner</div><div class="member-role">Chief Botanist</div></div>
<div class="member" style="left:448px;top:2258px"><div class="member-photo" role="img" aria-label="Portrait placeholder"></div><div class="member-name">Mark Osterby</div><div class="member-role">Chief Finance Officer</div></div>
<div class="member" style="left:771px;top:2258px"><div class="member-photo" role="img" aria-label="Portrait placeholder"></div><div class="member-name">Colin Ashdown</div><div class="member-role">Vice-President Marketing</div></div>
<div class="divider" style="top:2636px"></div>

<h2 class="section-title" style="top:2664px">Careers</h2>
<div class="vacancy" style="left:131px;top:2729px">Marketing and Sales Manager</div>
<div class="vacancy" style="left:448px;top:2729px">Software Engineer (Back-end)</div>
<div class="vacancy" style="left:769px;top:2729px">Agricultural Scientist</div>
<div class="vacancy" style="left:131px;top:2851px">Automation Engineer</div>
<div class="vacancy" style="left:448px;top:2851px">Growth Marketeer</div>
<div class="vacancy" style="left:769px;top:2851px">Data Science Engineer</div>

<footer class="site-footer">
  <div class="footer-col" style="left:76px;top:22px">
    <div class="footer-heading">Why don't you drop by?</div>
    <div class="footer-contact">Veldweg 14B,<br>6722AK, Bennekom<br>Email: info@valteradrones-example.com<br>Telephone: +31 6 12345678</div>
  </div>
  <div class="social"><span class="social-dot"></span><span>Netlink</span></div>
  <div class="footer-col" style="left:411px;top:22px">
    <div class="footer-heading">Crop monitoring</div>
    <ul class="footer-list"><li>Growth</li><li>Stress</li><li>Development</li><li>Diseases</li></ul>
    <div class="footer-heading" style="margin-top:38px">Markets</div>
    <ul class="footer-list"><li>Breeding</li><li>Young plant</li><li>Potplants</li><li>Cutflowers</li><li>Vegetables</li><li>Soft fruit</li></ul>
  </div>
  <div class="footer-col" style="left:619px;top:22px">
    <div class="footer-heading">Technology</div>
    <ul class="footer-list"><li>Aerial data collection</li><li>Artificial intelligence</li><li>Free data sets</li></ul>
    <div class="footer-heading" style="margin-top:56px">News &amp; downloads</div>
    <div class="footer-heading" style="margin-top:28px">Customer cases</div>
  </div>
  <div class="footer-col" style="left:857px;top:22px">
    <div class="footer-heading">About</div>
    <ul class="footer-list"><li>Vision</li><li>Company</li><li>Partners</li><li>Team</li><li>Career</li></ul>
    <div class="footer-heading" style="margin-top:20px">Free data sets</div>
    <div class="footer-heading" style="margin-top:28px">Contact</div>
  </div>
</footer>

</body>
</html>
```